LED Bulb Packaging

We require a retail box design so some led lighting. The concept must be uniform accross a nuimber of sizes with technical information and Actual bulb image replaceable.

```html
<!DOCTYPE html>
<html lang="en">
<head>
<meta charset="utf-8">
<title>LED Corn Light – Retail Box Dieline</title>
<link href="https://fonts.googleapis.com/css2?family=Roboto:wght@300;400;700;900&display=swap" rel="stylesheet">
<style>
  :root {
    --page: #ffffff;
    --plum: #7d2a6b;
    --magenta: #d4507f;
    --peach: #f7c3a6;
    --brand-blue: #1b4f9c;
    --band-gold: #e3a630;
    --tag-black: #111111;
    --tag-green: #7bbd4a;
    --tag-grey: #9c9c9c;
    --tag-sky: #8ec6ea;
    --icon-green: #5aa83a;
    --white: #ffffff;
  }
  html, body {
    margin: 0;
    padding: 0;
    width: 1200px;
    height: 542px;
    overflow: hidden;
    background: var(--page);
  }
  .dieline {
    display: block;
    width: 1200px;
    height: 542px;
    font-family: "Roboto", Arial, sans-serif;
  }
  .panel { fill: url(#panelGradient); }
  .brand-word { font-weight: 900; fill: var(--white); }
  .brand-sub { font-weight: 300; fill: var(--white); letter-spacing: .5px; }
  .brand-word--blue, .brand-sub--blue { fill: var(--brand-blue); }
  .tag-text { font-weight: 700; fill: var(--white); font-size: 5px; }
  .tag-sub { fill: var(--white); font-size: 2.6px; }
  .cert-mark { fill: none; stroke: var(--white); stroke-width: 1.1; }
  .note-text { fill: var(--white); font-size: 4.2px; }
  .note-title { fill: var(--white); font-size: 5px; font-weight: 700; }
  .icon-label { fill: var(--brand-blue); font-size: 2.8px; font-weight: 700; }
  .watt-text { fill: var(--brand-blue); font-weight: 900; font-size: 12px; }
  .spec-line { fill: var(--white); font-size: 3.4px; }
</style>
</head>
<body>
<svg class="dieline" viewBox="0 0 960 434" xmlns="http://www.w3.org/2000/svg">
  <defs>
    <linearGradient id="panelGradient" x1="0" y1="0.8" x2="1" y2="0.1">
      <stop offset="0" stop-color="#7d2a6b"/>
      <stop offset="0.45" stop-color="#d4507f"/>
      <stop offset="1" stop-color="#f7c3a6"/>
    </linearGradient>
    <linearGradient id="bulbGradient" x1="0" y1="0" x2="1" y2="1">
      <stop offset="0" stop-color="#f4f4f4"/>
      <stop offset="1" stop-color="#a9a9b2"/>
    </linearGradient>
    <linearGradient id="energyGradient" x1="0" y1="0" x2="0" y2="1">
      <stop offset="0" stop-color="#2e9b3e"/>
      <stop offset="0.5" stop-color="#f2d02c"/>
      <stop offset="1" stop-color="#d8262a"/>
    </linearGradient>
  </defs>

  <!-- Side panel (left) -->
  <g class="side-panel side-panel--left">
    <path class="panel" d="M30,200 L118,125 L383,125 L383,408 L150,408 L120,382 L62,362 L30,300 Z"/>
    <rect x="118" y="129" width="265" height="2" fill="var(--brand-blue)"/>
    <text class="brand-word brand-word--blue" x="221" y="152" font-size="17" text-anchor="middle">LED</text>
    <text class="brand-sub brand-sub--blue" x="221" y="160" font-size="4.5" text-anchor="middle">CORN LIGHT</text>
    <rect x="196" y="163" width="50" height="52" rx="6" fill="var(--white)"/>

    <g class="spec-tags">
      <path d="M60,208 h50 l5,6 l-5,6 h-50 Z" fill="var(--tag-black)"/>
      <text class="tag-text" x="85" y="214" text-anchor="middle">120LM/W</text>
      <text class="tag-sub" x="85" y="218" text-anchor="middle">Luminous efficacy</text>
      <path d="M60,225 h50 l5,6 l-5,6 h-50 Z" fill="var(--tag-green)"/>
      <text class="tag-text" x="85" y="231" text-anchor="middle">30000 HRS</text>
      <text class="tag-sub" x="85" y="235" text-anchor="middle">Average life</text>
      <path d="M60,242 h50 l5,6 l-5,6 h-50 Z" fill="var(--tag-grey)"/>
      <text class="tag-text" x="85" y="248" text-anchor="middle">80%</text>
      <text class="tag-sub" x="85" y="252" text-anchor="middle">Energy saving</text>
      <path d="M60,259 h50 l5,6 l-5,6 h-50 Z" fill="var(--tag-sky)"/>
      <text class="tag-text" x="85" y="267" text-anchor="middle">IP44</text>
    </g>

    <text class="brand-word" x="147" y="252" font-size="40">LED</text>
    <text class="brand-sub" x="148" y="268" font-size="11">CORN LIGHT</text>

    <rect x="258" y="195" width="88" height="88" rx="10" fill="url(#bulbGradient)" opacity=".9" role="img" aria-label="Product photo: LED corn light bulb"/>

    <rect x="60" y="287" width="323" height="16" fill="var(--band-gold)"/>
    <g class="cert-marks">
      <circle class="cert-mark" cx="160" cy="295" r="5"/>
      <circle class="cert-mark" cx="177" cy="295" r="5"/>
      <circle class="cert-mark" cx="194" cy="295" r="5"/>
      <circle class="cert-mark" cx="211" cy="295" r="5"/>
      <circle class="cert-mark" cx="228" cy="295" r="5"/>
      <rect class="cert-mark" x="240" y="290" width="12" height="10"/>
    </g>
  </g>

  <!-- Narrow side panel with notes -->
  <g class="side-panel side-panel--notes">
    <path class="panel" d="M383,130 L505,130 L505,408 L383,408 Z"/>
    <text class="note-title" x="388" y="205">Note:</text>
    <text class="note-text">
      <tspan x="388" y="211">- Before install or replace the lamps please cut off</tspan>
      <tspan x="388" y="216">  the power.</tspan>
      <tspan x="388" y="221">- After installed, when lamp work normal, please</tspan>
      <tspan x="388" y="226">  not take off the driver with electrified.</tspan>
      <tspan x="388" y="231">- After lighting a long time, the lamps can be reach</tspan>
      <tspan x="388" y="236">  60°C, please be careful to take off the lamps.</tspan>
      <tspan x="388" y="241">- Interior driver is constant current.</tspan>
      <tspan x="388" y="246">- Work temperature is -20~40°C.</tspan>
    </text>
    <g class="energy-label">
      <rect x="388" y="255" width="44" height="46" fill="var(--white)"/>
      <rect x="391" y="264" width="22" height="34" fill="url(#energyGradient)"/>
      <rect x="420" y="262" width="9" height="9" fill="var(--tag-black)"/>
    </g>
    <rect x="442" y="245" width="58" height="55" rx="8" fill="#f5d2c2" opacity=".8" role="img" aria-label="Faded product photo: LED corn light bulb"/>
  </g>

  <!-- Front panel -->
  <g class="front-panel">
    <path class="panel" d="M505,65 L828,65 L828,408 L812,408 Q808,392 792,390 L540,390 Q525,392 520,408 L505,408 Z"/>
    <rect class="hanger-tab" x="600" y="38" width="130" height="32" rx="8" fill="var(--brand-blue)"/>
    <path d="M640,66 Q640,94 665,94 Q690,94 690,66" fill="none" stroke="var(--white)" stroke-width="1" opacity=".6"/>

    <rect x="505" y="95" width="323" height="35" fill="var(--brand-blue)"/>
    <g class="feature-icons">
      <g transform="translate(556,100)"><rect width="24" height="25" fill="var(--white)"/><circle cx="12" cy="16" r="6" fill="var(--icon-green)"/><text class="icon-label" transform="rotate(180 12 5)" x="12" y="5" text-anchor="middle">Wide Angle</text></g>
      <g transform="translate(584,100)"><rect width="24" height="25" fill="var(--white)"/><circle cx="12" cy="16" r="6" fill="var(--white)"/><text class="icon-label" transform="rotate(180 12 5)" x="12" y="5" text-anchor="middle">No Flicker</text></g>
      <g transform="translate(612,100)"><rect width="24" height="25" fill="var(--white)"/><circle cx="12" cy="16" r="6" fill="var(--icon-green)"/><text class="icon-label" transform="rotate(180 12 5)" x="12" y="5" text-anchor="middle">Low Heat</text></g>
      <g transform="translate(640,100)"><rect width="24" height="25" fill="var(--white)"/><circle cx="12" cy="16" r="6" fill="var(--icon-green)"/><text class="icon-label" transform="rotate(180 12 5)" x="12" y="5" text-anchor="middle">Eye Care</text></g>
      <g transform="translate(668,100)"><rect width="24" height="25" fill="var(--white)"/><circle cx="12" cy="16" r="6" fill="var(--icon-green)"/><text class="icon-label" transform="rotate(180 12 5)" x="12" y="5" text-anchor="middle">Save Money</text></g>
      <g transform="translate(696,100)"><rect width="24" height="25" fill="var(--white)"/><circle cx="12" cy="16" r="6" fill="var(--icon-green)"/><text class="icon-label" transform="rotate(180 12 5)" x="12" y="5" text-anchor="middle">Eco Safe</text></g>
      <g transform="translate(724,100)"><rect width="24" height="25" fill="var(--white)"/><circle cx="12" cy="16" r="6" fill="var(--icon-green)"/><text class="icon-label" transform="rotate(180 12 5)" x="12" y="5" text-anchor="middle">Long Life</text></g>
      <g transform="translate(752,100)"><rect width="24" height="25" fill="var(--white)"/><circle cx="12" cy="16" r="6" fill="var(--icon-green)"/><text class="icon-label" transform="rotate(180 12 5)" x="12" y="5" text-anchor="middle">High Bright</text></g>
    </g>

    <g transform="rotate(180 665 152)">
      <text class="brand-word brand-word--blue" x="665" y="160" font-size="22" text-anchor="middle">LED</text>
      <text class="brand-sub brand-sub--blue" x="665" y="168" font-size="6" text-anchor="middle">CORN LIGHT</text>
    </g>

    <g class="spec-tags">
      <path d="M505,208 h50 l5,6 l-5,6 h-50 Z" fill="var(--tag-black)"/>
      <text class="tag-text" x="530" y="214" text-anchor="middle">120LM/W</text>
      <text class="tag-sub" x="530" y="218" text-anchor="middle">Luminous efficacy</text>
      <path d="M505,225 h50 l5,6 l-5,6 h-50 Z" fill="var(--tag-green)"/>
      <text class="tag-text" x="530" y="231" text-anchor="middle">30000 HRS</text>
      <text class="tag-sub" x="530" y="235" text-anchor="middle">Average life</text>
      <path d="M505,242 h50 l5,6 l-5,6 h-50 Z" fill="var(--tag-grey)"/>
      <text class="tag-text" x="530" y="248" text-anchor="middle">80%</text>
      <text class="tag-sub" x="530" y="252" text-anchor="middle">Energy saving</text>
      <path d="M505,259 h50 l5,6 l-5,6 h-50 Z" fill="var(--tag-sky)"/>
      <text class="tag-text" x="530" y="267" text-anchor="middle">IP44</text>
    </g>

    <text class="brand-word" x="592" y="252" font-size="40">LED</text>
    <text class="brand-sub" x="593" y="268" font-size="11">CORN LIGHT</text>

    <rect x="703" y="195" width="88" height="88" rx="10" fill="url(#bulbGradient)" opacity=".9" role="img" aria-label="Product photo: LED corn light bulb"/>

    <rect x="505" y="287" width="323" height="16" fill="var(--band-gold)"/>
    <g class="cert-marks">
      <circle class="cert-mark" cx="585" cy="295" r="5"/>
      <circle class="cert-mark" cx="602" cy="295" r="5"/>
      <circle class="cert-mark" cx="619" cy="295" r="5"/>
      <circle class="cert-mark" cx="636" cy="295" r="5"/>
      <circle class="cert-mark" cx="653" cy="295" r="5"/>
      <rect class="cert-mark" x="665" y="290" width="12" height="10"/>
    </g>
  </g>

  <!-- Side panel (right) -->
  <g class="side-panel side-panel--right">
    <path class="panel" d="M828,125 L895,125 L930,180 L930,330 L895,392 L850,410 L828,410 Z"/>
    <g class="wattage-icon">
      <path d="M878,226 A20,20 0 1 1 872,248" fill="none" stroke="var(--brand-blue)" stroke-width="3"/>
      <text class="watt-text" x="890" y="246" text-anchor="middle">27W</text>
      <path d="M879,258 Q876,268 882,274 L898,274 Q904,268 901,258" fill="none" stroke="var(--white)" stroke-width="1.4"/>
      <rect x="883" y="276" width="14" height="3" fill="var(--white)"/>
      <rect x="885" y="281" width="10" height="3" fill="var(--white)"/>
    </g>
    <text class="spec-line" x="872" y="296">30000 hrs</text>
    <text class="spec-line" x="892" y="296">IP44</text>
    <text class="spec-line" x="902" y="296">120lm</text>
  </g>
</svg>
</body>
</html>
```